Buch-/eBook-Cover für Bücher aus den Bereichen europäisches Mittelalter und Kathedralen
Zielgruppe
Wir sind ein Buchverlag. Die Zielgruppe der Bücher sind Menschen, die sich für das europäische Mittelalter und Kathedralen begeistern.
Aufgabenstellung
Ich brauche einen Cover (Paperback, Hardcover, E-Book, Audiobook, Mockup) für die englische Ausgabe des Buches 'Arcs of Devotion. The Riddle of Gothic Minster Layout Sketches

```html
<!DOCTYPE html>
<html lang="en">
<head>
<meta charset="utf-8">
<title>Arcs of Devotion – Book Cover</title>
<link href="https://fonts.googleapis.com/css2?family=Inter:wght@300;400&display=swap" rel="stylesheet">
<style>
  :root {
    --backdrop: #e4e5e0;
    --cover-yellow: #e9e04b;
    --diagram-light: #ddd443;
    --diagram-deep: #a9a33a;
    --ink: #2a2a28;
  }
  html, body {
    margin: 0;
    padding: 0;
    width: 1200px;
    height: 900px;
    overflow: hidden;
    background: var(--backdrop);
  }
  .canvas {
    position: relative;
    width: 1200px;
    height: 900px;
  }
  .cover {
    position: absolute;
    left: 340px;
    top: 60px;
    width: 520px;
    height: 780px;
    background: var(--cover-yellow);
    color: var(--ink);
    font-family: "Inter", Arial, sans-serif;
    box-shadow: 0 10px 30px rgba(0,0,0,0.12);
  }
  .author-first,
  .author-last {
    position: absolute;
    left: 48px;
    right: 44px;
    display: flex;
    justify-content: space-between;
    font-size: 38px;
    font-weight: 300;
    line-height: 1;
  }
  .author-first { top: 46px; }
  .author-last { bottom: 30px; }
  .title {
    position: absolute;
    left: 52px;
    top: 178px;
    margin: 0;
    font-size: 27px;
    font-weight: 300;
    line-height: 1.15;
    letter-spacing: -0.5px;
    transform: scaleX(0.86);
    transform-origin: left top;
    text-transform: uppercase;
  }
  .diagram {
    position: absolute;
    left: 140px;
    top: 250px;
    width: 330px;
    height: 330px;
    border-radius: 50%;
    background: radial-gradient(circle at 55% 45%, var(--diagram-light) 0%, var(--diagram-light) 45%, var(--diagram-deep) 100%);
    opacity: 0.85;
  }
  .subtitle {
    position: absolute;
    left: 56px;
    top: 610px;
    margin: 0;
    font-size: 15px;
    font-weight: 300;
    line-height: 1.2;
    text-transform: uppercase;
    transform: scaleX(0.86);
    transform-origin: left top;
  }
  .subtitle-mark {
    position: absolute;
    left: 110px;
    top: 680px;
    width: 3px;
    height: 3px;
    background: var(--ink);
    border-radius: 50%;
  }
</style>
</head>
<body>
  <main class="canvas">
    <article class="cover">
      <div class="author-first" aria-label="Nora Helene">
        <span>N</span><span>O</span><span>R</span><span>A</span><span>&nbsp;</span><span>H</span><span>E</span><span>L</span><span>E</span><span>N</span><span>E</span>
      </div>
      <h1 class="title">Arcs of<br>Devotion</h1>
      <div class="diagram" role="img" aria-label="Medieval compass construction drawing: a circle crossed by arcs and a diameter, with lettered construction points"></div>
      <p class="subtitle">The Riddle of<br>Gothic Minster<br>Layout Sketches</p>
      <span class="subtitle-mark"></span>
      <div class="author-last" aria-label="Weis">
        <span>W</span><span>E</span><span>I</span><span>S</span>
      </div>
    </article>
  </main>
</body>
</html>
```